Residential improvers, A Quiet Harbor 9 Me *

Quiet Harbor 9 Me is a real estate company specializing in turning unloved properties into improved, happy places to live. We specialize in thoughtfully-improved residential properties for buyers or renters. Our company needs a business card that reflects the renovated homes we create using green and Feng Shui principles,

Please disregard the images we submitted. We are looking for an abstract, sophisticated elegant design. No eggs in a nest ... nothing cute. The image can be soft.
Updates

Aloha (hello) all designers. We are a serious property investment/improvement company. We strive to be unique, renovating with style and elegance. Our business card must portray the same message. We thought the nest and flower might be "it" ... clearly it's not, once we saw what you submitted. Please revisit the brief as it was modified yesterday. Mahalo for your input! We look forward to hearing from all designers that have been invited.

Industry/Entity Type

Real Estate Development

Contact Information for Business Card

We will have separate business cards for
1) Corabeth Danvers 808-555-0173 corabeth@mailtrove.net
2) Trina Vasquell 808-555-0196 trinavasquell@mailtrove.net
** can we add the website later ... in the process of approval.
Investors * Renovators * Connectors

Font styles to use
Sans Serif

Colors
cadf82

Requirements
Must have
• a feng shui feel ... modern. Color - green with black print.
Nice to have
• A Quiet Harbor 9 Me

```html
<!DOCTYPE html>
<html lang="en">
<head>
<meta charset="utf-8">
<title>Quiet Harbor 9 Me – Business Card</title>
<link rel="stylesheet" href="https://fonts.googleapis.com/css2?family=Montserrat:wght@400;700&family=Questrial&display=swap">
<style>
  :root {
    --page: #ffffff;
    --ink: #000000;
    --paper: #ffffff;
    --leaf: #cadf82;
    --leaf-deep: #bcd46e;
    --shadow: rgba(0, 0, 0, 0.28);
  }
  * { margin: 0; padding: 0; box-sizing: border-box; }
  html, body {
    width: 1000px;
    height: 1200px;
    overflow: hidden;
    background: var(--page);
  }
  .canvas {
    position: relative;
    width: 1000px;
    height: 1200px;
    background: var(--page);
    font-family: "Questrial", "Century Gothic", sans-serif;
  }
  .card {
    position: absolute;
    top: 197px;
    width: 419px;
    height: 698px;
    box-shadow: 0 40px 40px -14px var(--shadow);
    overflow: hidden;
  }
  .card--back { left: 53px; background: var(--ink); color: var(--paper); }
  .card--front { left: 547px; background: var(--paper); color: var(--ink); }

  /* brand lockup */
  .brand {
    position: absolute;
    display: flex;
    align-items: center;
    gap: 14px;
    font-family: "Questrial", "Century Gothic", sans-serif;
    font-weight: 400;
    line-height: 1.05;
    white-space: nowrap;
  }
  .brand__dot {
    width: 38px;
    height: 38px;
    border-radius: 50%;
    background: var(--leaf);
    flex: none;
  }
  .brand__name { font-size: 34px; letter-spacing: -0.5px; }
  .card--back .brand { left: 92px; top: 430px; color: var(--paper); }
  .card--front .brand { left: 98px; top: 240px; color: var(--ink); }

  .website-line {
    position: absolute;
    left: 0;
    right: 0;
    top: 630px;
    text-align: center;
    font-size: 20px;
    letter-spacing: 0.3px;
  }
  .website-line strong { font-family: "Montserrat", sans-serif; font-weight: 700; font-size: 19px; }

  /* name band */
  .name-band {
    position: absolute;
    left: -2px;
    top: 394px;
    width: 334px;
    height: 106px;
    border: 2px solid var(--leaf);
    border-left: none;
    border-radius: 0 53px 53px 0;
  }
  .person {
    position: absolute;
    left: 56px;
    top: 418px;
    font-family: "Montserrat", sans-serif;
    line-height: 1;
  }
  .person__first { display: block; font-weight: 700; font-size: 30px; letter-spacing: 0.2px; }
  .person__last { display: block; font-family: "Questrial", sans-serif; font-weight: 400; font-size: 29px; margin-top: 2px; }

  .contact-list {
    position: absolute;
    left: 54px;
    top: 512px;
    list-style: none;
    font-size: 18.5px;
    letter-spacing: 0.3px;
  }
  .contact-list li {
    display: flex;
    align-items: center;
    height: 29px;
  }
  .contact-list svg {
    width: 18px;
    height: 18px;
    margin-right: 13px;
    flex: none;
  }
</style>
</head>
<body>
<main class="canvas">

  <section class="card card--back" aria-label="Card back">
    <div class="brand">
      <span class="brand__dot"></span>
      <span class="brand__name">Quiet Harbor<br>9 Me</span>
    </div>
    <p class="website-line">www.<strong>quietharbor9me</strong>.com</p>
  </section>

  <section class="card card--front" aria-label="Card front">
    <div class="brand">
      <span class="brand__dot"></span>
      <span class="brand__name">Quiet Harbor<br>9 Me</span>
    </div>

    <div class="name-band"></div>
    <h1 class="person">
      <span class="person__first">Corabeth</span>
      <span class="person__last">Danvers</span>
    </h1>

    <ul class="contact-list">
      <li>
        <svg viewBox="0 0 18 18" aria-hidden="true">
          <rect x="5" y="2" width="8" height="14" rx="1.5" fill="var(--leaf-deep)"/>
          <rect x="6.5" y="4" width="5" height="5" fill="#fff"/>
          <line x1="11" y1="0" x2="11" y2="2" stroke="var(--leaf-deep)" stroke-width="1.5"/>
        </svg>
        808-555-0173
      </li>
      <li>
        <svg viewBox="0 0 18 18" aria-hidden="true">
          <rect x="1" y="4" width="16" height="11" fill="none" stroke="var(--leaf-deep)" stroke-width="1.6"/>
          <polyline points="1,4 9,11 17,4" fill="none" stroke="var(--leaf-deep)" stroke-width="1.6"/>
        </svg>
        corabeth@mailtrove.net
      </li>
      <li>
        <svg viewBox="0 0 18 18" aria-hidden="true">
          <circle cx="9" cy="9" r="7.5" fill="none" stroke="var(--leaf-deep)" stroke-width="1.6"/>
          <ellipse cx="9" cy="9" rx="3.2" ry="7.5" fill="none" stroke="var(--leaf-deep)" stroke-width="1.4"/>
          <line x1="1.5" y1="9" x2="16.5" y2="9" stroke="var(--leaf-deep)" stroke-width="1.4"/>
        </svg>
        www.quietharbor9me.com
      </li>
    </ul>
  </section>

</main>
</body>
</html>
```